KD Summit Fitness personal training needs a new Business Card design for 2016

Business Card design:
Our current business card is very plain
We are bringing on our first team member next year and thought its a perfect time to have a new face lift for our company!

We are a Personal Training business "KD Summit Fitness" who specializes in strength and conditioning / weightloss training,
We also run a yearly Bootcamp called "Ferocity Bootcamps", this is our Logo Design which we are looking for

The pink and blue in the logo are our business colours, how ever we don't want those colours to heavily dominate the card.

We are looking for a business card which is eye catching, and creative.

I am open to suggestions and any designs :)

Logo Design:

For our Logo Design we are looking for a bright, energetic logo, preferably a word logo which portrays strength and high intensity
If it has icon's etc in it thats fine again im open for suggestions :)
The Logo Design is for our Bootcamp which runs yearly
The bootcamp is called "Ferocity Bootcamp"

Target Market(s)

Age 20-40
Individuals who want to look great and have more energy

Industry/Entity Type

Business

Contact Information for Business Card

On the front
KD Summit Fitness Derwin Okoye Personal Training / Bootcamps / Pilates / Nutrition Healthy mind, Healthy body, Ultimate lifestyle < our slogan
Icons for the following
Email:
Mobile:
Facebook:
Instagram:

On the back we would like to include somewhere
"Show this card to receive 50% off your first 30min pt session"
"Valid to one user only"

Logo Text

Ferocity Bootcamp

Font styles to use
Serif

Colors
e34197
0255a3
000000
ffffff

Requirements
Must have
• - Icons for instagram, facebook, email and mobile phone
• - Slogan: Healthy mind, Healthy body, Ultimate lifestyle
• - What we offer: Personal Training , Bootcamps, Pilates, Nutrition
• - Logo
• -
Nice to have
• - Our 50% offer on the back
• - a place for a photo
Should not have
• - Pink and Blue everywhere

```html
<!DOCTYPE html>
<html lang="en">
<head>
<meta charset="utf-8">
<title>KD Summit Fitness – Business Card</title>
<link href="https://fonts.googleapis.com/css2?family=Cinzel:wght@600&family=Oswald:wght@400;500;600&display=swap" rel="stylesheet">
<style>
  :root{
    --stage:#e9e6e1;
    --card:#0b0b0c;
    --pink:#e34197;
    --pink-soft:#e88ac4;
    --blue:#0255a3;
    --blue-bright:#2f86d6;
    --grey:#a9a9ad;
    --white:#ffffff;
  }
  *{box-sizing:border-box;margin:0;padding:0}
  html,body{width:1200px;height:1023px;overflow:hidden;background:var(--stage)}
  .canvas{position:relative;width:1200px;height:1023px}
  .card{position:absolute;left:220px;width:760px;height:434px;border-radius:6px;overflow:hidden;
        background:var(--card);box-shadow:0 10px 30px rgba(0,0,0,.25)}
  .card--front{top:48px}
  .card--back{top:540px}

  /* front */
  .front__mark{position:absolute;right:40px;top:40px;width:330px;height:330px;border-radius:12px;
        background:radial-gradient(ellipse at 50% 45%,#3a3a3d 0%,#222224 55%,rgba(11,11,12,0) 80%);opacity:.8}
  .front__brand{position:absolute;right:44px;top:30px;
        font:500 15px/1 'Oswald',sans-serif;letter-spacing:.08em;color:var(--blue-bright);text-transform:uppercase}
  .front__name{position:absolute;left:52px;top:120px;font:600 40px/1 'Cinzel',serif;color:var(--pink-soft);letter-spacing:.04em}
  .front__services{position:absolute;left:54px;top:172px;font:500 14px/1 'Oswald',sans-serif;color:var(--grey);
        letter-spacing:.1em;text-transform:uppercase}
  .contact{position:absolute;left:54px;top:210px;list-style:none}
  .contact__item{display:flex;align-items:center;gap:10px;font:500 17px/1 'Oswald',sans-serif;color:var(--white);
        letter-spacing:.08em;text-transform:uppercase;margin-bottom:9px}
  .contact__icon{width:18px;height:18px;border-radius:3px;background:var(--blue);display:flex;align-items:center;justify-content:center}
  .contact__icon--social{background:var(--pink)}
  .contact__gap{height:10px}
  .front__slogan{position:absolute;left:54px;bottom:34px;font:600 18px/1 'Oswald',sans-serif;color:var(--blue-bright);
        letter-spacing:.09em;text-transform:uppercase}

  /* back */
  .back__texture{position:absolute;inset:0;background:radial-gradient(ellipse at 40% 40%,#2e2e30 0%,#1a1a1c 50%,#0d0d0e 100%)}
  .back__brand{position:absolute;left:0;right:0;top:128px;text-align:center;
        font:600 42px/1 'Oswald',sans-serif;color:var(--blue-bright);letter-spacing:.06em;text-transform:uppercase}
  .back__offer{position:absolute;left:0;right:0;top:252px;text-align:center;font:500 22px/1.45 'Oswald',sans-serif;color:var(--pink-soft);letter-spacing:.03em}
</style>
</head>
<body>
<main class="canvas">

  <section class="card card--front" aria-label="Business card front">
    <div class="front__mark" role="img" aria-label="Large faint grunge-textured brand decoration"></div>
    <div class="front__brand">KD Summit Fitness</div>
    <h1 class="front__name">Derwin Okoye</h1>
    <p class="front__services">Personal Training | Bootcamps | Pilates | Nutrition</p>
    <ul class="contact">
      <li class="contact__item"><span class="contact__icon">
        <svg width="10" height="12" viewBox="0 0 10 12"><rect x="1.5" y="0.5" width="7" height="11" rx="1.5" fill="none" stroke="#fff"/><circle cx="5" cy="9.5" r=".8" fill="#fff"/></svg>
      </span>0198 765 432</li>
      <li class="contact__item"><span class="contact__icon">
        <svg width="12" height="9" viewBox="0 0 12 9"><rect x=".5" y=".5" width="11" height="8" fill="none" stroke="#fff"/><path d="M.5 .5 6 5l5.5-4.5" fill="none" stroke="#fff"/></svg>
      </span>coach@kdsummitfit.com</li>
      <li class="contact__item"><span class="contact__icon">
        <svg width="12" height="12" viewBox="0 0 12 12"><circle cx="6" cy="6" r="5" fill="none" stroke="#fff"/><path d="M1 6h10M6 1c-2.5 3-2.5 7 0 10M6 1c2.5 3 2.5 7 0 10" fill="none" stroke="#fff" stroke-width=".8"/></svg>
      </span>www.kdsummitfitness.com.au</li>
      <li class="contact__gap"></li>
      <li class="contact__item"><span class="contact__icon contact__icon--social"></span>kdsummitfitness</li>
      <li class="contact__item"><span class="contact__icon contact__icon--social"></span>kdsummitfitness</li>
    </ul>
    <p class="front__slogan">Healthy Mind • Healthy Body • Ultimate Lifestyle</p>
  </section>

  <section class="card card--back" aria-label="Business card back">
    <div class="back__texture" role="img" aria-label="Dark grunge stone texture"></div>
    <p class="back__brand">KD Summit Fitness</p>
    <p class="back__offer">Show this card to receive 50% off your first 30min pt session<br>Valid to one user only</p>
  </section>

</main>
</body>
</html>
```